Webdesign für Gravierwerkstatt
Zielgruppe
Das Unternehmen ist eine Gravierwerkstatt - die Zielgruppe sind sowohl private als auch gewerbliche Kunden und Vereine für Einzelauftrgäge oder Kleinserien für Gravuren
Aufgabenstellung
- modernes Layout
- Farbgebung blau, hellblau, Grau, weiß
- übersichtliche Darstellung der angebotenen Leistungen
- kein Kontaktformular
- nicht zu viele Bilder
- es existiert kein richtiges Logo, (es kann aber das Handwerkszeichen wiederverwendet werden)
- Names des Unternehmens 'Gravierwerkstatt Brenner'
- Meisterwerkstatt

```html
<!DOCTYPE html>
<html lang="de">
<head>
<meta charset="utf-8">
<title>Gravierwerkstatt Brenner – Meisterbetrieb</title>
<link href="https://fonts.googleapis.com/css2?family=Inter:wght@400;500;600;700&display=swap" rel="stylesheet">
<style>
:root{
  --blue:#2563eb;
  --blue-soft:#eef3fd;
  --ink:#0f172a;
  --text:#475569;
  --muted:#94a3b8;
  --line:#e8edf5;
  --bg-soft:#f7f9fc;
  --navy:#0f1427;
}
*{box-sizing:border-box;margin:0;padding:0}
html,body{width:1200px;height:2407px;overflow:hidden}
body{font-family:'Inter',sans-serif;color:var(--ink);background:#fff;position:relative}
.abs{position:absolute}
.hero{position:absolute;left:0;top:0;width:1200px;height:794px;background:linear-gradient(115deg,#f8fafc 0%,#f5f8fd 55%,#e6eefc 100%)}
.nav{left:67px;top:21px;width:1066px;height:67px;background:#fff;border-radius:10px;box-shadow:0 2px 10px rgba(15,23,42,.05)}
.brand{left:22px;top:18px;display:flex;align-items:center;gap:12px}
.brand-dot{width:30px;height:30px;border-radius:50%;background:var(--blue-soft);border:1px solid #c7d6f7}
.brand-name{font-weight:600;font-size:17px;line-height:19px}
.brand-sub{font-size:9.5px;letter-spacing:2px;color:var(--text);font-weight:500}
.menu{left:420px;top:0;display:flex;gap:34px;height:67px;align-items:center;font-size:14px;color:#334155}
.menu .on{color:var(--blue);position:relative;height:67px;display:flex;align-items:center}
.menu .on:after{content:"";position:absolute;left:0;right:0;bottom:0;height:2px;background:var(--blue)}
.call{right:22px;top:16px;height:34px;padding:0 16px;border-radius:17px;background:var(--blue-soft);color:var(--blue);font-size:13px;display:flex;align-items:center;gap:7px}
.pill{left:67px;top:177px;height:30px;padding:0 14px;border-radius:15px;border:1px solid #dbe5f7;background:#fff;color:var(--blue);font-size:12px;font-weight:500;display:flex;align-items:center;gap:8px}
h1{left:67px;top:228px;font-size:48px;line-height:55px;font-weight:700;letter-spacing:-1px}
h1 span{color:var(--blue)}
.lead{left:67px;top:416px;width:440px;font-size:15px;line-height:24.5px;color:var(--text)}
.btn{height:44px;border-radius:6px;font-size:14px;font-weight:500;display:flex;align-items:center;gap:10px;padding:0 20px}
.btn-p{left:67px;top:522px;background:var(--blue);color:#fff}
.btn-s{left:304px;top:522px;background:#fff;color:var(--blue);border:1px solid #dbe5f7}
.feats{left:67px;top:612px;display:flex;align-items:center;font-size:12px;color:#1e293b;line-height:15px}
.feat{display:flex;align-items:center;gap:12px;padding-right:27px;margin-right:27px;border-right:1px solid var(--line);height:32px;white-space:nowrap}
.feat:last-child{border:0}
.photo{left:634px;top:160px;width:499px;height:500px;border-radius:14px;background:linear-gradient(160deg,#2b5e66 0%,#1d2b33 40%,#5a3a1c 75%,#c5771e 100%);box-shadow:0 10px 30px rgba(15,23,42,.15)}
.float{left:925px;top:626px;width:247px;height:60px;background:#fff;border-radius:10px;box-shadow:0 8px 24px rgba(15,23,42,.1);display:flex;align-items:center;gap:12px;padding-left:20px;font-size:11.5px;font-weight:500;white-space:nowrap}
.ic{width:32px;height:32px;border-radius:50%;background:var(--blue-soft);display:flex;align-items:center;justify-content:center;flex:none}
h2{font-size:25px;font-weight:600;text-align:center;letter-spacing:-.3px}
.sec-t{left:0;width:1200px;top:873px}
.sec-s{left:0;width:1200px;top:918px;text-align:center;font-size:15px;line-height:23.5px;color:var(--text)}
.card{top:1018px;width:324px;height:231px;border:1px solid var(--line);border-radius:12px;background:#fff;padding:27px}
.card .sq{width:40px;height:40px;border-radius:8px;background:var(--blue-soft);display:flex;align-items:center;justify-content:center}
.card h3{font-size:17px;font-weight:600;margin:24px 0 12px}
.card li{list-style:none;font-size:14px;color:var(--text);display:flex;align-items:center;gap:10px;height:30px}
.trad{left:0;top:1329px;width:1200px;height:423px;background:var(--bg-soft)}
.trad h2{margin-top:80px}
.trad p{width:770px;margin:22px auto 0;text-align:center;font-size:16.5px;line-height:23.5px;color:var(--text)}
.trad p b{color:var(--ink);font-weight:600}
.stars{display:flex;justify-content:center;gap:8px;margin-top:32px}
.contact{left:67px;top:1834px;width:1066px;height:422px;border-radius:18px;background:radial-gradient(circle at 85% 25%,#1e3a8a 0%,#14204a 35%,var(--navy) 75%);color:#fff;box-shadow:0 20px 40px rgba(15,23,42,.2)}
.contact h4{font-size:25px;font-weight:600;letter-spacing:-.3px}
.c-left{left:53px;top:50px}
.row{display:flex;gap:17px;margin-top:28px}
.row .ic{width:40px;height:40px;background:rgba(255,255,255,.09)}
.lbl{font-size:11.5px;letter-spacing:1.5px;color:#94a3b8;font-weight:500;margin-bottom:4px}
.val{font-size:16px;line-height:23.5px}
.divider{left:559px;top:52px;width:1px;height:317px;background:rgba(255,255,255,.12)}
.c-right{left:614px;top:50px;width:399px}
.note{margin-top:33px;height:79px;border-radius:10px;border:1px solid rgba(255,255,255,.14);background:rgba(255,255,255,.04);display:flex;gap:14px;padding:18px 18px;font-size:13px;line-height:21px;color:#cbd5e1}
.hours{margin-top:20px}
.h{display:flex;justify-content:space-between;height:58px;align-items:center;font-size:15px;border-bottom:1px solid rgba(255,255,255,.12);color:#e2e8f0}
.h b{font-weight:500;color:#fff}
.h:last-child{border:0}
.h .off{color:#64748b;font-weight:400}
.footer{left:0;top:2337px;width:1200px;height:70px;background:var(--bg-soft);border-top:1px solid var(--line);font-size:12px;color:#64748b}
.footer .l{left:87px;top:27px}
.footer .r{right:87px;top:27px;display:flex;gap:20px}
</style>
</head>
<body>
<section class="hero">
  <header class="nav abs">
    <div class="brand abs"><div class="brand-dot"></div><div><div class="brand-name">Gravierwerkstatt Brenner</div><div class="brand-sub">MEISTERBETRIEB</div></div></div>
    <nav class="menu abs"><span class="on">Startseite</span><span>Leistungen</span><span>Über uns</span><span>Kontakt</span></nav>
    <div class="call abs"><svg width="13" height="13" viewBox="0 0 24 24" fill="none" stroke="currentColor" stroke-width="2"><path d="M22 16.9v3a2 2 0 0 1-2.2 2A19.8 19.8 0 0 1 2.1 4.2 2 2 0 0 1 4.1 2h3a2 2 0 0 1 2 1.7l.5 3a2 2 0 0 1-.6 1.8L7.7 9.8a16 16 0 0 0 6.5 6.5l1.3-1.3a2 2 0 0 1 1.8-.6l3 .5a2 2 0 0 1 1.7 2z"/></svg>Anrufen</div>
  </header>
  <div class="pill abs"><svg width="12" height="12" viewBox="0 0 24 24" fill="none" stroke="currentColor" stroke-width="2"><circle cx="12" cy="8" r="6"/><path d="M8.5 13 7 22l5-3 5 3-1.5-9"/></svg>Meisterwerkstatt für Gravuren</div>
  <h1 class="abs">Präzise Gravuren für<br><span>Unternehmen, Vereine<br>und Privatkunden</span></h1>
  <p class="lead abs">Gravierwerkstatt Brenner fertigt hochwertige Gravuren, Schilder, Pokale, Stempel und individuelle Handgravuren – zuverlässig, präzise und persönlich.</p>
  <div class="btn btn-p abs"><svg width="14" height="14" viewBox="0 0 24 24" fill="none" stroke="currentColor" stroke-width="2"><path d="M5 12h14M13 6l6 6-6 6"/></svg>Jetzt Kontakt aufnehmen</div>
  <div class="btn btn-s abs">Leistungen ansehen<svg width="12" height="12" viewBox="0 0 24 24" fill="none" stroke="currentColor" stroke-width="2"><path d="m9 6 6 6-6 6"/></svg></div>
  <div class="feats abs">
    <div class="feat"><svg width="18" height="18" viewBox="0 0 24 24" fill="none" stroke="#2563eb" stroke-width="1.8"><path d="M12 2 4 5v6c0 5 3.4 9.4 8 11 4.6-1.6 8-6 8-11V5z"/><path d="m9 12 2 2 4-4"/></svg>Meisterwerkstatt</div>
    <div class="feat"><svg width="18" height="18" viewBox="0 0 24 24" fill="none" stroke="#2563eb" stroke-width="1.8"><path d="m12 2 9 5v10l-9 5-9-5V7z"/><path d="M3 7l9 5 9-5M12 12v10"/></svg>Einzelaufträge &amp;<br>Kleinserien</div>
    <div class="feat"><svg width="20" height="18" viewBox="0 0 24 24" fill="none" stroke="#2563eb" stroke-width="1.8"><circle cx="9" cy="7" r="4"/><path d="M2 21v-2a5 5 0 0 1 5-5h4a5 5 0 0 1 5 5v2M16 3a4 4 0 0 1 0 8M22 21v-2a5 5 0 0 0-3-4.6"/></svg>Für Firmen, Vereine<br>&amp; Privatkunden</div>
  </div>
  <div class="photo abs" role="img" aria-label="Lasergravurmaschine bei der Arbeit mit Funkenflug über einer Metallplatte"></div>
  <div class="float abs"><div class="ic"><svg width="15" height="15" viewBox="0 0 24 24" fill="none" stroke="#2563eb" stroke-width="2"><path d="M6 9H4a2 2 0 0 1 0-4h2M18 9h2a2 2 0 0 0 0-4h-2M6 3h12v7a6 6 0 0 1-12 0zM12 16v4M8 21h8"/></svg></div>Schilder · Pokale · Lasergravur</div>
</section>

<h2 class="sec-t abs">Unsere Leistungen</h2>
<p class="sec-s abs">Von der klassischen Handwerkskunst bis zur hochmodernen Lasertechnik<br>bieten wir ein breites Spektrum an Gravurarbeiten an.</p>

<div class="card abs" style="left:87px">
  <div class="sq"><svg width="18" height="18" viewBox="0 0 24 24" fill="none" stroke="#2563eb" stroke-width="1.8"><circle cx="12" cy="12" r="3"/><path d="M19.4 15a1.7 1.7 0 0 0 .3 1.8l.1.1a2 2 0 1 1-2.8 2.8l-.1-.1a1.7 1.7 0 0 0-2.9 1.2V21a2 2 0 0 1-4 0v-.1a1.7 1.7 0 0 0-2.9-1.2l-.1.1a2 2 0 1 1-2.8-2.8l.1-.1A1.7 1.7 0 0 0 3.1 14H3a2 2 0 0 1 0-4h.1a1.7 1.7 0 0 0 1.2-2.9l-.1-.1a2 2 0 1 1 2.8-2.8l.1.1A1.7 1.7 0 0 0 10 3.1V3a2 2 0 0 1 4 0v.1a1.7 1.7 0 0 0 2.9 1.2l.1-.1a2 2 0 1 1 2.8 2.8l-.1.1A1.7 1.7 0 0 0 20.9 10H21a2 2 0 0 1 0 4h-.1a1.7 1.7 0 0 0-1.5 1z"/></svg></div>
  <h3>Gravuren</h3>
  <ul>
    <li><svg width="16" height="16" viewBox="0 0 24 24" fill="none" stroke="#2563eb" stroke-width="1.6"><circle cx="12" cy="12" r="10"/><path d="m8 12 3 3 5-5"/></svg>Schilder- und Industriegravuren</li>
    <li><svg width="16" height="16" viewBox="0 0 24 24" fill="none" stroke="#2563eb" stroke-width="1.6"><circle cx="12" cy="12" r="10"/><path d="m8 12 3 3 5-5"/></svg>Hochpräzise Lasergravur</li>
    <li><svg width="16" height="16" viewBox="0 0 24 24" fill="none" stroke="#2563eb" stroke-width="1.6"><circle cx="12" cy="12" r="10"/><path d="m8 12 3 3 5-5"/></svg>Pokale und Vereinsbedarf</li>
  </ul>
</div>
<div class="card abs" style="left:438px">
  <div class="sq"><svg width="18" height="18" viewBox="0 0 24 24" fill="none" stroke="#2563eb" stroke-width="1.8"><path d="m12 19 7-7 3 3-7 7zM18 13l-1.5-7.5L2 2l3.5 14.5L13 18zM2 2l7.6 7.6"/><circle cx="11" cy="11" r="2"/></svg></div>
  <h3>Handgravuren</h3>
  <ul>
    <li><svg width="16" height="16" viewBox="0 0 24 24" fill="none" stroke="#2563eb" stroke-width="1.6"><circle cx="12" cy="12" r="10"/><path d="m8 12 3 3 5-5"/></svg>Individuelle Trauringe</li>
    <li><svg width="16" height="16" viewBox="0 0 24 24" fill="none" stroke="#2563eb" stroke-width="1.6"><circle cx="12" cy="12" r="10"/><path d="m8 12 3 3 5-5"/></svg>Kunstvolle Monogramme</li>
  </ul>
</div>
<div class="card abs" style="left:789px">
  <div class="sq"><svg width="18" height="18" viewBox="0 0 24 24" fill="none" stroke="#2563eb" stroke-width="1.8"><rect x="3" y="3" width="18" height="18" rx="2"/><path d="M3 9h18M3 15h18M9 3v18M15 3v18"/></svg></div>
  <h3>Sonstige Leistungen</h3>
  <ul>
    <li><svg width="16" height="16" viewBox="0 0 24 24" fill="none" stroke="#2563eb" stroke-width="1.6"><circle cx="12" cy="12" r="10"/><path d="m8 12 3 3 5-5"/></svg>Personalisierte Stempel</li>
    <li><svg width="16" height="16" viewBox="0 0 24 24" fill="none" stroke="#2563eb" stroke-width="1.6"><circle cx="12" cy="12" r="10"/><path d="m8 12 3 3 5-5"/></svg>Detailreiche Zinngravuren</li>
  </ul>
</div>

<section class="trad abs">
  <h2>Tradition trifft auf Moderne</h2>
  <p>Seit der Gründung unserer Werkstatt stehen Qualität, Zuverlässigkeit und die Liebe zum Detail an erster Stelle. Als eingetragener <b>Meisterbetrieb</b> verbinden wir jahrzehntelange Erfahrung im klassischen Handwerk mit innovativen Technologien.</p>
  <p>Unser Anspruch ist es, für jeden Kunden – ob Industrieunternehmen, Verein oder Privatperson – die perfekte Lösung zu finden und langlebige Werte zu schaffen. Wir beraten Sie persönlich und setzen Ihre Vorgaben millimetergenau um.</p>
  <div class="stars">
    <svg width="19" height="19" viewBox="0 0 24 24" fill="#cbd5e1"><path d="m12 2 3 6.5 7 .8-5.2 4.8 1.4 7L12 17.6 5.8 21l1.4-7L2 9.3l7-.8z"/></svg>
    <svg width="19" height="19" viewBox="0 0 24 24" fill="#cbd5e1"><path d="m12 2 3 6.5 7 .8-5.2 4.8 1.4 7L12 17.6 5.8 21l1.4-7L2 9.3l7-.8z"/></svg>
    <svg width="19" height="19" viewBox="0 0 24 24" fill="#cbd5e1"><path d="m12 2 3 6.5 7 .8-5.2 4.8 1.4 7L12 17.6 5.8 21l1.4-7L2 9.3l7-.8z"/></svg>
  </div>
</section>

<section class="contact abs">
  <div class="c-left abs">
    <h4>Kontaktieren Sie uns</h4>
    <div class="row" style="margin-top:32px"><div class="ic"><svg width="17" height="17" viewBox="0 0 24 24" fill="none" stroke="#fff" stroke-width="1.7"><path d="M20 10c0 6-8 12-8 12s-8-6-8-12a8 8 0 0 1 16 0z"/><circle cx="12" cy="10" r="3"/></svg></div><div><div class="lbl">ADRESSE</div><div class="val">Musterstraße 123<br>12345 Musterstadt</div></div></div>
    <div class="row"><div class="ic"><svg width="17" height="17" viewBox="0 0 24 24" fill="none" stroke="#fff" stroke-width="1.7"><path d="M22 16.9v3a2 2 0 0 1-2.2 2A19.8 19.8 0 0 1 2.1 4.2 2 2 0 0 1 4.1 2h3a2 2 0 0 1 2 1.7l.5 3a2 2 0 0 1-.6 1.8L7.7 9.8a16 16 0 0 0 6.5 6.5l1.3-1.3a2 2 0 0 1 1.8-.6l3 .5a2 2 0 0 1 1.7 2z"/></svg></div><div><div class="lbl">TELEFON</div><div class="val">0123 456 789</div></div></div>
    <div class="row"><div class="ic"><svg width="17" height="17" viewBox="0 0 24 24" fill="none" stroke="#fff" stroke-width="1.7"><rect x="2" y="4" width="20" height="16" rx="2"/><path d="m22 7-10 6L2 7"/></svg></div><div><div class="lbl">E-MAIL</div><div class="val">info@gravierwerkstatt-brenner.de</div></div></div>
  </div>
  <div class="divider abs"></div>
  <div class="c-right abs">
    <h4>Öffnungszeiten</h4>
    <div class="note"><svg width="18" height="18" viewBox="0 0 24 24" fill="none" stroke="#60a5fa" stroke-width="1.8" style="flex:none"><circle cx="12" cy="12" r="10"/><path d="M12 6v6l4 2"/></svg>Bitte vereinbaren Sie für aufwendige Beratungen vorab einen Termin.</div>
    <div class="hours">
      <div class="h"><span>Montag - Donnerstag</span><b>08:00 - 17:00</b></div>
      <div class="h"><span>Freitag</span><b>08:00 - 14:00</b></div>
      <div class="h"><span>Samstag &amp; Sonntag</span><span class="off">Geschlossen</span></div>
    </div>
  </div>
</section>

<footer class="footer abs">
  <div class="l abs">© 2023 Gravierwerkstatt Brenner. Alle Rechte vorbehalten.</div>
  <div class="r abs"><span>Impressum</span><span>Datenschutz</span><span>Barrierefreiheit</span></div>
</footer>
</body>
</html>
```